New Wrestling company needs a website

We need a website design for a new wrestling company in Australia that will be running 3-4 events per year. Wrestling company is Coralline Elite Grappling (CEG).

The design of the logo is in place and can be provided, and I have purchased the website domain.

A detailed description of the intent and purpose of this company can be provided.

The aim would be to have around 5 specific pages on CEG, with two standard “about” and “contact” pages. E.g.
- About CEG (focus and purpose of the company)
- CEG Events (specific focus on events run by CEG)
- CEG News (news and stories on wrestling’s across Oceania)
- CEG Media (where to watch CEG and our partners))
- CEG Partners and Sponsors (partner and affiliate information)
- CEG Power Rankings (top 10 ranked wrestlers from Oceania which is updated weekly)
- CEG fans (highlighting how to become part of CEG as a fan)
- Contact CEG
Updates

The logo design should now be included in the brief, please feel free to reach out to me directly if you can't access it or require any other information.

Target Market(s)

Wrestling Fans

Industry/Entity Type

Sport / Wrestling

Coding

Coded - Design and coding required

Number of Pages Required

5+ page

Requirements
Must have
• A Wrestling and or Sports feel to the website design

```html
<!DOCTYPE html>
<html lang="en">
<head>
<meta charset="utf-8">
<title>Coralline Elite Grappling</title>
<link rel="stylesheet" href="https://fonts.googleapis.com/css2?family=Exo+2:wght@400;500;600;700&family=Roboto:wght@500;700;900&display=swap">
<style>
:root{
  --bg:#132738;
  --bg-deep:#0d1c29;
  --footer:#0f1d2a;
  --accent:#2ca9e8;
  --accent-dark:#1b6fc2;
  --text:#ffffff;
  --muted:#c9d3dc;
  --line:#3a78b8;
}
*{margin:0;padding:0;box-sizing:border-box}
html,body{width:1200px;height:3711px;overflow:hidden}
body{
  position:relative;
  background:radial-gradient(ellipse at 50% 20%,#1c3a52 0%,var(--bg) 45%,var(--bg-deep) 100%);
  color:var(--text);
  font-family:"Exo 2",sans-serif;
}
.abs{position:absolute}
.accent{color:var(--accent)}
.heading{font-family:"Roboto",sans-serif;font-weight:700;text-transform:uppercase;letter-spacing:.5px}
.center{text-align:center;left:0;width:1200px}

/* nav */
.brand{left:99px;top:22px;font-family:"Exo 2",sans-serif;font-weight:700;font-size:30px;color:var(--accent);display:flex;align-items:center;gap:8px}
.brand .dot{width:14px;height:14px;border-radius:50%;background:var(--accent)}
.nav{top:38px;font-size:11px;font-weight:600;text-transform:uppercase;letter-spacing:.3px}
.nav a{position:absolute;color:#fff;text-decoration:none;white-space:nowrap}
.nav a.active{color:var(--accent)}
.user-btn{left:935px;top:26px;width:40px;height:40px;border-radius:50%;background:linear-gradient(#38b4ea,#1b6fc2);border:2px solid #8fd3f5;display:flex;align-items:center;justify-content:center}
.btn-outline{border:2px solid var(--line);border-radius:22px;color:#fff;font-size:11px;font-weight:600;text-transform:uppercase;display:flex;align-items:center;justify-content:center;letter-spacing:.5px}
.btn-fill{background:linear-gradient(#3cb8ee,#1d73c6);border:2px solid #9bd9f7;border-radius:22px;color:#fff;font-size:11px;font-weight:600;text-transform:uppercase;display:flex;align-items:center;justify-content:center;letter-spacing:.5px;box-shadow:0 4px 12px rgba(0,0,0,.4)}

/* hero */
.hero{left:99px;top:94px;width:1001px;height:436px;border:2px solid var(--line);background:linear-gradient(180deg,#1a2340 0%,#3b3a6a 35%,#22304c 60%,#101a28 100%)}
.hero-title{top:385px;font-family:"Roboto",sans-serif;font-weight:700;font-size:42px;letter-spacing:.5px}
.hero-sub{top:440px;font-family:"Roboto",sans-serif;font-weight:500;font-size:23px}
.arrow{width:30px;height:30px;border-radius:50%;background:#fff;display:flex;align-items:center;justify-content:center}

/* text */
.section-title{font-size:34px}
.lead{font-size:16px;line-height:23px}
.small{font-size:12px;line-height:22px;color:var(--muted)}

/* quote band */
.quote{left:99px;width:1001px;height:138px;background:linear-gradient(90deg,#1d6fc2 0%,#2b93db 55%,#3bb8ee 100%);border:1px solid #6ec8f2;border-radius:90px 0 90px 0;display:flex;align-items:center;justify-content:center;text-align:center;padding:0 120px;font-size:15px;font-weight:600;line-height:18px;letter-spacing:.3px}

/* events */
.bullets{left:200px;top:1226px;width:380px;list-style:none}
.bullets li{position:relative;padding-left:22px;font-size:12.5px;line-height:19px;margin-bottom:18px;color:#e6edf2}
.bullets li::before{content:"";position:absolute;left:0;top:3px;width:11px;height:11px;border-radius:50%;background:var(--accent)}

/* partners */
.card-img{height:156px;width:250px}
.card-title{font-size:15.5px;font-weight:600;color:var(--accent);line-height:19px;width:250px}
.card-text{font-size:10.5px;line-height:19px;color:var(--muted);width:250px}
.read{font-size:10px;font-weight:700;color:var(--accent);text-transform:uppercase;letter-spacing:.5px}

/* media */
.media-box{width:250px;height:124px;border:1px solid var(--line);background:rgba(10,24,36,.6);display:flex;align-items:center;justify-content:center;text-align:center;font-size:15px;font-weight:600;line-height:19px;padding:20px 24px 0}
.media-mark{width:250px;text-align:center;font-weight:700;font-size:34px;color:var(--accent)}

/* footer */
.footer{left:0;top:3355px;width:1200px;height:356px;background:var(--footer)}
.footer-title{font-size:15px;font-weight:600;color:var(--accent);text-transform:uppercase}
.footer-link{font-size:10.5px;color:#e3e9ee}
.input{left:749px;top:3462px;width:250px;height:35px;border:1px solid var(--line);border-radius:18px;font-size:10.5px;color:#cfd8df;display:flex;align-items:center;padding-left:18px}
.social{width:36px;height:36px;border-radius:50%;border:1.5px solid var(--line)}
.social.active{background:linear-gradient(#3cb8ee,#1d73c6)}
</style>
</head>
<body>

<!-- header -->
<div class="abs brand"><span class="dot"></span>CEG</div>
<nav class="abs nav" style="left:0;width:1200px">
  <a class="active" style="left:285px">Home</a>
  <a style="left:341px">About Us</a>
  <a style="left:421px">Events</a>
  <a style="left:489px">News</a>
  <a style="left:545px">Media</a>
  <a style="left:605px">Partners &amp; Sponsors</a>
  <a style="left:758px">Power Ranking</a>
  <a style="left:873px">Fans</a>
</nav>
<div class="abs user-btn">
  <svg width="14" height="14" viewBox="0 0 14 14" fill="none" stroke="#fff" stroke-width="1.4"><circle cx="7" cy="4.5" r="2.6"/><path d="M2 13c0-3 2.3-4.8 5-4.8s5 1.8 5 4.8"/></svg>
</div>
<div class="abs btn-outline" style="left:988px;top:28px;width:111px;height:36px">Contact Us</div>

<!-- hero -->
<div class="abs hero" role="img" aria-label="Packed wrestling arena with a lit ring under stage lights"></div>
<div class="abs center hero-title">LOREM IPSUM IS SIMPLY DUMMY TEXT</div>
<div class="abs center hero-sub">PRINTING AND TYPESETTING INDUSTRY IPSUM</div>
<div class="abs arrow" style="left:84px;top:297px"><svg width="10" height="10" viewBox="0 0 10 10"><path d="M6.5 1.5 3 5l3.5 3.5" fill="none" stroke="#1a3a5a" stroke-width="1.5"/></svg></div>
<div class="abs arrow" style="left:1085px;top:297px"><svg width="10" height="10" viewBox="0 0 10 10"><path d="M3.5 1.5 7 5 3.5 8.5" fill="none" stroke="#1a3a5a" stroke-width="1.5"/></svg></div>

<!-- welcome -->
<h1 class="abs center heading section-title" style="top:582px">Welcome to <span class="accent">CEG</span></h1>
<p class="abs lead" style="left:200px;width:800px;top:635px;text-align:center">Coralline Elite Grappling (CEG) has been created as a <span class="accent">DESTINATION EVENT PRO WRESTLING</span> company for <span class="accent">OCEANIA.</span> We want to collaborate with other wrestling companies (Oceania and International) in our event, media and fan outcomes.</p>
<p class="abs small" style="left:190px;width:820px;top:719px;text-align:center;color:#fff">The creator and Managing Director of CEG is an experienced and successful Australian Sporting Administrator with 20 plus years' experience in sport as a CEO and COO in three major Australian sports, and a deep passion for the wrestling industry.</p>
<div class="abs btn-fill" style="left:536px;top:792px;width:128px;height:38px">Discover More</div>

<div class="abs quote" style="top:893px">“The creator and Managing Director of CEG is an experienced and successful Australian Sporting Administrator with 20 plus years' experience in sport as a CEO and COO in three major Australian sports, and a deep passion for the wrestling industry.”</div>

<!-- events -->
<h2 class="abs heading section-title" style="left:200px;top:1115px"><span class="accent">CEG</span> Events</h2>
<p class="abs" style="left:200px;top:1167px;width:360px;font-size:15.5px;font-weight:500;line-height:19px">The first CEG event will be announced in late March 2022.</p>
<ul class="abs bullets">
  <li>Putting on 3 to 4 key annual events in partnership with other wrestling companies, in locations in Oceania that seek to draw visitation to their cities.</li>
  <li>Giving Wrestling talent and wrestling promotions in Oceania an opportunity to shine.</li>
  <li>Commercially partner with leading international wrestling promotions.</li>
</ul>
<div class="abs btn-outline" style="left:200px;top:1420px;width:125px;height:38px">Explore More</div>
<div class="abs" style="left:613px;top:1095px;width:388px;height:388px;border-radius:50%;border:14px solid #8c959c;background:radial-gradient(circle,#2a7fcf 0%,#1d63aa 60%,#174f8a 100%)" role="img" aria-label="Wrestling ring seen through a large circular frame"></div>
<div class="abs" style="left:723px;top:1205px;width:168px;height:168px;border-radius:50%;border:14px solid #8c959c"></div>

<div class="abs quote" style="top:1548px">"We are the bridge between the local promotions in Oceania to elevate their talent, and International promotions wanting to engage Oceania Fans with their international talent and brand."</div>

<!-- partners -->
<h2 class="abs center heading section-title" style="top:1740px"><span class="accent">CEG</span> Partners</h2>
<p class="abs center" style="top:1792px;font-size:15.5px;font-weight:500">The first partners, internationally and Australian, are expected to be announced in late March 2022.</p>
<p class="abs" style="left:290px;width:620px;top:1822px;text-align:center;font-size:11px;line-height:15px;color:#e3e9ee">To our partners, companies or wrestling talent, CEG is about OPPORTUNITY – wrestling or business. Wrestling partners will be from three key areas in our Event build.</p>

<div class="abs card-img" style="left:200px;top:1879px;background:linear-gradient(135deg,#5a3a2a,#2b2220 60%,#7a5a40)" role="img" aria-label="Group of international wrestlers posing together"></div>
<div class="abs card-img" style="left:474px;top:1879px;background:linear-gradient(135deg,#1b3f8a,#4a2c5a 55%,#8a6a50)" role="img" aria-label="Australian wrestlers posing with a championship belt"></div>
<div class="abs card-img" style="left:749px;top:1879px;background:linear-gradient(135deg,#2a1416,#8a1e22 55%,#3a1a1a)" role="img" aria-label="Independent wrestlers in action in the ring"></div>

<div class="abs card-title" style="left:200px;top:2050px">International Wrestling Organisations</div>
<div class="abs card-title" style="left:474px;top:2050px">Australian Wrestling Companies</div>
<div class="abs card-title" style="left:749px;top:2050px">Free Agent Independent International Wrestlers</div>

<p class="abs card-text" style="left:200px;top:2102px">We will look to partner with as many International Wrestling Companies for mutually beneficial outcomes, whether wrestling related...</p>
<p class="abs card-text" style="left:474px;top:2102px">Where possible we will elevate the talent and the promotions of the best Australian, NZ and other wrestling companies in Oceania...</p>
<p class="abs card-text" style="left:749px;top:2102px">CEG events will be an opportunity for the strong base of international independent talent to appear as well.</p>

<div class="abs read" style="left:200px;top:2174px">Read More</div>
<div class="abs read" style="left:474px;top:2174px">Read More</div>
<div class="abs read" style="left:749px;top:2173px">Read More</div>
<div class="abs btn-outline" style="left:537px;top:2233px;width:126px;height:38px">Discover More</div>

<div class="abs quote" style="top:2333px">“This combination will lead to 3-4 quality events per annum with an emphasis on showcasing professional wrestling through our quality broadcasting and highly engaging fan experience model at events, backed by a unique Membership model wrestling fans and a weekly media show”.</div>

<!-- media -->
<h2 class="abs center heading section-title" style="top:2527px"><span class="accent">CEG</span> Media</h2>
<p class="abs" style="left:270px;width:660px;top:2581px;text-align:center;font-size:15.5px;font-weight:500;line-height:19px">CEG Media is anticipated to launch in June 2022, shortly after the announcement of our first major CEG event.</p>
<p class="abs" style="left:290px;width:620px;top:2635px;text-align:center;font-size:11px;line-height:17px;color:#e3e9ee">Between our events, we will seek to keep a consistent engagement via launching a new wrestling media show (TV, Radio or Podcast) to cover</p>

<div class="abs media-box" style="left:200px;top:2714px">Oceania talent in overseas promotions,</div>
<div class="abs media-box" style="left:474px;top:2714px">Oceania wrestling promotions and their local events and</div>
<div class="abs media-box" style="left:749px;top:2714px">CEG Events – the build to each CEG event and recap post event.</div>
<div class="abs media-mark" style="left:200px;top:2689px">CEG</div>
<div class="abs media-mark" style="left:474px;top:2689px">CEG</div>
<div class="abs media-mark" style="left:749px;top:2689px">CEG</div>
<div class="abs btn-fill" style="left:536px;top:2868px;width:128px;height:38px">Discover Media</div>

<!-- fans -->
<div class="abs" style="left:200px;top:2969px;width:387px;height:318px;background:linear-gradient(160deg,#3a3fa8 0%,#5b2f8a 40%,#1a1f3a 100%)" role="img" aria-label="Cheering crowd of fans at a wrestling event"></div>
<h2 class="abs heading section-title" style="left:612px;top:2962px"><span class="accent">CEG</span> Fans</h2>
<p class="abs" style="left:612px;top:3012px;font-size:15.5px;font-weight:500">CEG Membership will launch in July 2022.</p>
<p class="abs card-text" style="left:612px;top:3052px;width:395px">The core business is CEG Events, with supporting CEG Media and touring CEG champions.</p>
<p class="abs card-text" style="left:612px;top:3108px;width:395px">But the heartbeat of our events at CEG will be our CEG Fans – real fans of professional wrestling.</p>
<p class="abs card-text" style="left:612px;top:3164px;width:395px">Our aim at CEG is to create a sense of belonging to professional wrestling fans in Oceania through membership and engagement like it does for other sports and clubs in Australia.</p>
<div class="abs btn-outline" style="left:612px;top:3249px;width:125px;height:38px">Read More</div>

<!-- footer -->
<footer class="abs footer"></footer>
<div class="abs" style="left:200px;top:3446px;font-weight:700;font-size:54px;color:var(--accent);display:flex;align-items:center;gap:14px"><span style="width:22px;height:22px;border-radius:50%;background:var(--accent)"></span>CEG</div>

<div class="abs footer-title" style="left:475px;top:3416px">Quick Links</div>
<div class="abs footer-link" style="left:475px;top:3459px">Home</div>
<div class="abs footer-link" style="left:475px;top:3481px">About Us</div>
<div class="abs footer-link" style="left:475px;top:3504px">Events</div>
<div class="abs footer-link" style="left:475px;top:3526px">News</div>
<div class="abs footer-link" style="left:475px;top:3549px">Media</div>
<div class="abs footer-link" style="left:565px;top:3459px">Partners &amp; Sponsors</div>
<div class="abs footer-link" style="left:565px;top:3481px">Power Ranking</div>
<div class="abs footer-link" style="left:565px;top:3504px">Fans</div>
<div class="abs footer-link" style="left:565px;top:3526px">Contact Us</div>

<div class="abs footer-title" style="left:749px;top:3416px">Stay in Touch!</div>
<div class="abs input">Enter Your Email...</div>
<div class="abs btn-fill" style="left:749px;top:3512px;width:102px;height:34px;font-size:10px">Submit</div>

<div class="abs" style="left:200px;top:3618px;font-size:10.5px;color:#e3e9ee">©2022 <span class="accent">CORALLINE ELITE GRAPPLING.</span> All Rights Reserved. &nbsp;&nbsp;&nbsp; Privacy Policy &nbsp;&nbsp; | &nbsp;&nbsp; Terms of Use</div>

<div class="abs social" style="left:749px;top:3607px"></div>
<div class="abs social active" style="left:793px;top:3607px"></div>
<div class="abs social" style="left:837px;top:3607px"></div>
<div class="abs social" style="left:881px;top:3607px"></div>

<svg class="abs" style="left:1087px;top:3610px" width="26" height="30" viewBox="0 0 26 30" fill="none" stroke="#2ca9e8" stroke-width="2.2" stroke-linejoin="round"><path d="M13 2 24 28 13 21 2 28Z"/></svg>

</body>
</html>
```